Verpackungsdesign für Outdoor-Produkt
Lurvo suchte ein neues Design in der Kategorie Verpackungen und hat ein Projekt auf gestaltwerk-portal.de gestartet.
Zielgruppe
Wir verkaufen einzigartige Outdoor Produkte. Der Feuerstahl richtet sich an alle, die gerne in der Natur übernachten und beim Feuermachen noch selbst Hand anlegen wollen. Die Zielgruppe interessiert sich für Bushcraft & Survival, ist größtenteils Männlich und zwischen 30-40 Jahre alt.
Aufgabenstellung
Auf die obere Seite der Verpackung sollen das Logo und der Produktname platziert werden. Das Produkt gibt es in zwei Varianten, deshalb auch zwei verschiedene Namen.
Auf der vorderen Seite sollen die Features hervorgehoben werden. Dafür zum Beispiel ein passendes Icon finden und die Eigenschaft dazu (Beispiel: 'Flammen'-Icon, Bis zu 20.000 Zündungen garantiert).
An den Seiten links und rechts reicht das Logo.
Auf die hintere Seite kommt das Impressum.
Die Verpackung besteht aus braunem Karton.

```html
<!DOCTYPE html>
<html lang="de">
<head>
<meta charset="utf-8">
<title>Lurvo Feuerstahl – Verpackung Stanzkontur</title>
<link href="https://fonts.googleapis.com/css2?family=Roboto+Slab:wght@300;400;700;800&family=Open+Sans:wght@400&display=swap" rel="stylesheet">
<style>
  :root {
    --paper: #ffffff;
    --ink: #111111;
    --cut: #1a1a1a;
    --fold: #e53935;
    --caption: #a9a9a9;
  }
  html, body { margin: 0; padding: 0; overflow: hidden; background: var(--paper); }
  .canvas { position: relative; width: 873px; height: 1200px; overflow: hidden; background: var(--paper); font-family: "Roboto Slab", serif; color: var(--ink); }
  .dieline { position: absolute; left: 0; top: 0; }
  .cut { fill: none; stroke: var(--cut); stroke-width: 0.6; }
  .fold { fill: none; stroke: var(--fold); stroke-width: 0.6; }
  .icon { fill: none; stroke: var(--ink); stroke-width: 1; stroke-linecap: round; stroke-linejoin: round; }

  .product-name { position: absolute; right: 234px; top: 178px; text-align: right; line-height: 1; }
  .product-name .line-main { font-weight: 800; font-size: 14px; letter-spacing: 0.2px; }
  .product-name .line-variant { font-weight: 300; font-size: 12.5px; margin-top: 2px; }

  .brand-mark { position: absolute; left: 336px; width: 200px; top: 222px; text-align: center; font-weight: 700; font-size: 24px; letter-spacing: 3px; }

  .imprint { position: absolute; left: 217px; width: 439px; top: 400px; text-align: center; font-size: 6.3px; line-height: 1.25; }
  .imprint p { margin: 0; }
  .imprint .company { font-weight: 700; margin-bottom: 8px; }
  .imprint .address { margin-bottom: 8px; }
  .imprint .web { font-weight: 700; }

  .feature { position: absolute; top: 486px; width: 90px; text-align: center; }
  .feature svg { display: block; margin: 0 auto 3px; }
  .feature h3 { margin: 0; font-size: 6.8px; font-weight: 400; line-height: 1.15; text-transform: uppercase; }
  .feature p { margin: 3px 0 0; font-size: 5.2px; line-height: 1.25; }

  .caption { position: absolute; left: 0; width: 873px; top: 1129px; text-align: center; font-family: "Open Sans", sans-serif; font-size: 6.6px; letter-spacing: 1px; color: var(--caption); }
</style>
</head>
<body>
<div class="canvas">

  <svg class="dieline" width="873" height="1200" viewBox="0 0 873 1200" aria-hidden="true">
    <!-- top closure flap with dust ears -->
    <path class="cut" d="M220,89 H654"/>
    <path class="cut" d="M220,92 C190,95 165,108 165,128 V155 Q165,161 172,161 H210 L217,166"/>
    <path class="cut" d="M654,92 C684,95 707,108 707,128 V155 Q707,161 700,161 H662 L656,166"/>
    <path class="fold" d="M220,89 V166 M654,89 V166 M220,166 H654"/>

    <!-- top panel -->
    <path class="cut" d="M220,166 L215,170 V280 L222,284"/>
    <path class="cut" d="M654,166 L658,170 V280 L651,284"/>
    <path class="fold" d="M222,284 H651"/>

    <!-- second panel with tabs -->
    <path class="cut" d="M222,290 H167 V356 H219 Q222,356 222,360"/>
    <path class="cut" d="M651,290 H705 V356 H654 Q651,356 651,360"/>
    <path class="fold" d="M222,284 V363 M651,284 V363 M217,363 H656"/>

    <!-- back panel with side flaps -->
    <path class="cut" d="M217,363 H140 L129,367 H57 V404 H47 V436 H57 V472 H129 L140,476 H217"/>
    <path class="cut" d="M656,363 H733 L744,367 H816 V404 H826 V436 H816 V472 H744 L733,476 H656"/>
    <path class="fold" d="M140,363 V476 M129,367 V472 M733,363 V476 M744,367 V472 M217,363 V476 M656,363 V476 M217,476 H656"/>
    <path class="cut" d="M217,403 H227 V436 H217"/>
    <path class="cut" d="M656,403 H645 V436 H656"/>

    <!-- feature panel with tabs -->
    <path class="cut" d="M225,476 Q222,483 218,483 H171 V549 H221 L225,553 H648 L652,549 H701 V483 H655 Q651,483 648,476"/>
    <path class="fold" d="M225,476 V553 M648,476 V553"/>
  </svg>

  <div class="product-name">
    <div class="line-main">FEUERSTAHL</div>
    <div class="line-variant">BASIC</div>
  </div>

  <div class="brand-mark">LURVO</div>

  <div class="imprint">
    <p class="company">Lurvo</p>
    <p class="address">Am Holzhafen 4 · 22111 Hamburg · Deutschland</p>
    <p>kundenservice@lurvo-outdoor.de</p>
    <p class="web">www.lurvo-outdoor.de</p>
  </div>

  <div class="feature" style="left:253px">
    <svg class="icon" width="14" height="16" viewBox="0 0 14 16"><path d="M7,1 C9,5 12,7 12,10.5 A5,5 0 0 1 2,10.5 C2,8 4,7 4.5,4.5 C6,6 6,7.5 7,8.5 C8,7 8,4 7,1Z"/></svg>
    <h3>3000 °C heiße<br>Funken</h3>
    <p>Mehr als 20.000<br>Zündungen garantiert</p>
  </div>

  <div class="feature" style="left:335px">
    <svg class="icon" width="26" height="16" viewBox="0 0 26 16"><path d="M2,5 L24,10 L23.3,12.6 L1.3,7.6 Z"/></svg>
    <h3>XXL<br>Zündstab</h3>
    <p>12,7 cm lang,<br>1,27 cm Durchmesser</p>
  </div>

  <div class="feature" style="left:421px;width:104px">
    <svg class="icon" width="24" height="16" viewBox="0 0 24 16"><path d="M3,12 L17,3 Q21,1.5 21.5,4 Q22,6 19,7.5 L5,14 Q2.5,14.5 3,12Z M8,10.5 L17,5"/><circle cx="18.5" cy="4.5" r="1"/></svg>
    <h3>Survival Striker</h3>
    <p>Hochwertiger 8Cr13MoV Stahl,<br>läßt sich im Notfall sogar zu<br>Mini Messer schärfen</p>
  </div>

  <div class="feature" style="left:523px;width:100px">
    <svg class="icon" width="64" height="16" viewBox="0 0 64 16"><path d="M2,5 H14 A2,2 0 1 0 12,3 M2,9 H18 A2,2 0 1 1 16,11 M6,13 H12"/><path d="M32,4 C34,7 35,9 35,11 A3,3 0 0 1 29,11 C29,9 30,7 32,4Z M38,2 C39.5,4 40,5 40,6 A2,2 0 0 1 36,6 C36,5 36.5,4 38,2Z"/><path d="M54,2 V14 M48.8,5 L59.2,11 M48.8,11 L59.2,5 M52,3 L54,4.5 L56,3 M52,13 L54,11.5 L56,13"/></svg>
    <h3>Wind-/Wasser-/<br>Kälte-Resist</h3>
    <p>Schutz bei<br>allen Witterungen</p>
  </div>

  <div class="caption">PACKAGING „LURVO“ ABMESSUNG 50 X 35 &nbsp;X 195 MM · WWW.LURVO-OUTDOOR.DE</div>
</div>
</body>
</html>
```